Business Card Design

New business card design

Target Market(s)

Residential & Commercial Property Managers

Industry/Entity Type

Plumbing Services

Contact Information for Business Card

Name - Owen Tredgold, title - Director, Phone Number - 0431 862 507, email - owen@rvb-plumbing.com.au, Company ABN - 73 215 904 386,

Font styles to use
Sans Serif

Colors
0054AA
0677BA
7BADD7
CADEEF
E8F1F8

```html
<!DOCTYPE html>
<html lang="en">
<head>
<meta charset="utf-8">
<title>RVB Plumbing Services – Business Card</title>
<link rel="stylesheet" href="https://fonts.googleapis.com/css2?family=Open+Sans:ital,wght@0,300;0,400;1,400&display=swap">
<style>
  :root {
    --backdrop: #ece6df;
    --card-black: #050607;
    --logo-white: #ffffff;
    --muted-taupe: #7d7266;
    --detail-grey: #a39a8f;
    --frame-line: #6b6055;
    --blue-light: #8ccbea;
    --blue-bright: #3bbdec;
    --ink-navy: #143150;
  }
  * { margin: 0; padding: 0; box-sizing: border-box; }
  html, body {
    width: 1200px; height: 900px; overflow: hidden;
    background: var(--backdrop);
    font-family: "Open Sans", Arial, sans-serif;
  }
  .canvas { position: relative; width: 1200px; height: 900px; }
  .card {
    position: absolute; left: 280px; width: 640px; height: 366px;
    background: var(--card-black); overflow: hidden;
    box-shadow: 0 10px 28px rgba(60, 40, 20, 0.28);
  }
  .card--front { top: 48px; }
  .card--back { top: 486px; }
  .card__art { position: absolute; inset: 0; width: 100%; height: 100%; }

  .wave-area {
    position: absolute; left: 0; bottom: 0; width: 310px; height: 130px;
    background: linear-gradient(30deg, var(--blue-light), var(--blue-bright));
  }

  .wordmark {
    position: absolute; display: flex; align-items: center; gap: 14px;
    color: var(--logo-white); font-weight: 300; line-height: 1;
    letter-spacing: 2px;
  }
  .wordmark__dot { border-radius: 50%; background: var(--blue-bright); }
  .tagline {
    position: absolute; color: var(--muted-taupe); font-weight: 400;
    text-transform: lowercase; white-space: nowrap;
  }

  .card--front .wordmark { left: 150px; top: 78px; font-size: 150px; }
  .card--front .wordmark__dot { width: 26px; height: 26px; }
  .card--front .tagline { left: 170px; top: 250px; font-size: 13px; letter-spacing: 13px; }
  .abn {
    position: absolute; left: 350px; top: 322px; width: 200px;
    text-align: center; font-size: 14px; color: var(--ink-navy); white-space: nowrap;
  }

  .card--back .wordmark { left: 90px; top: 60px; font-size: 110px; }
  .card--back .wordmark__dot { width: 20px; height: 20px; }
  .card--back .tagline { left: 100px; top: 190px; font-size: 10px; letter-spacing: 8px; }
  .divider-dots { position: absolute; left: 205px; top: 214px; display: flex; gap: 8px; }
  .divider-dots span { width: 4px; height: 4px; border-radius: 50%; background: var(--detail-grey); }

  .contact {
    position: absolute; left: 370px; top: 150px; width: 240px;
    text-align: center; color: var(--detail-grey);
  }
  .contact__name { font-size: 26px; font-weight: 400; }
  .contact__role { font-size: 17px; font-style: italic; margin-top: 2px; }
  .contact__line {
    display: flex; align-items: center; justify-content: center; gap: 7px;
    font-size: 15px; font-weight: 300; margin-top: 10px; white-space: nowrap;
  }
  .contact__line svg { width: 13px; height: 13px; fill: var(--detail-grey); }
</style>
</head>
<body>
<main class="canvas">

  <section class="card card--front" aria-label="Business card front">
    <svg class="card__art" viewBox="0 0 640 366" aria-hidden="true">
      <defs>
        <linearGradient id="bandBlue" x1="0" y1="0" x2="1" y2="0">
          <stop offset="0" stop-color="#8ccbea"/>
          <stop offset="1" stop-color="#3bbdec"/>
        </linearGradient>
      </defs>
      <path d="M0,344 L322,344 C338,344 336,312 356,312 L548,312 C568,312 566,344 584,344 L640,344 L640,366 L0,366 Z" fill="url(#bandBlue)"/>
    </svg>
    <div class="wordmark">rvb<span class="wordmark__dot"></span></div>
    <p class="tagline">plumbing services</p>
    <p class="abn">ABN - 73 215 904 386</p>
  </section>

  <section class="card card--back" aria-label="Business card back">
    <div class="wave-area" role="img" aria-label="Decorative blue water wave graphic"></div>
    <svg class="card__art" viewBox="0 0 640 366" aria-hidden="true">
      <rect x="16" y="16" width="608" height="334" fill="none" stroke="#6b6055" stroke-width="1"/>
    </svg>
    <div class="wordmark">rvb<span class="wordmark__dot"></span></div>
    <p class="tagline">plumbing services</p>
    <div class="divider-dots"><span></span><span></span><span></span></div>
    <div class="contact">
      <p class="contact__name">Owen Tredgold</p>
      <p class="contact__role">Director</p>
      <p class="contact__line">
        <svg viewBox="0 0 24 24" aria-hidden="true"><path d="M6.6 10.8a15.1 15.1 0 0 0 6.6 6.6l2.2-2.2a1 1 0 0 1 1-.25 11.4 11.4 0 0 0 3.6.57 1 1 0 0 1 1 1V20a1 1 0 0 1-1 1A17 17 0 0 1 3 4a1 1 0 0 1 1-1h3.5a1 1 0 0 1 1 1c0 1.25.2 2.45.57 3.57a1 1 0 0 1-.25 1z"/></svg>
        0431 862 507
      </p>
      <p class="contact__line">
        <svg viewBox="0 0 24 24" aria-hidden="true"><path d="M2 5h20v14H2z M4 7v.5l8 5 8-5V7l-8 5z" fill-rule="evenodd"/></svg>
        owen@rvb-plumbing.com.au
      </p>
    </div>
  </section>

</main>
</body>
</html>
```